New Shop front sign with 2 x window sign designs

I require a New shop sign for a retail store. with 2 x window design for printing onto korvalite material. it must be bright and fresh. please see images of sizes required.

Please see a similar logo for the top sign, it shows qLumo. but we require the same or similar (better) design saying Bramble den. It will be on a plain backgroung of white, with the slogan at the bottom most items below £1. and also a seperate area for the "small family owned business" I just want a plain simple top sign that is professional and stylish. please see the upload area wher i have added the qlumo logo. i look forward to your designs coming through to me,

This is for a retail store, and it needs to reflect our cheap prices.

Retail

• For the top sign, it must say "The Bramble Den" in bigger text as the main sign. and under the main words, we need to have a slogan similar to "Big Brands Better Prices - Most products under £1"
• Also on the top sign, I would like to add "local family run business"
• The backround needs to reflect cheap prices, maybe like £ signs and good artwork.
• The first window sign, needs to be about our cheap mr dandow ice cream, where it will be sold for 89p. it must have a cornet cone with soft icecream top. with good artwork, advertising the low price of only 99p.
• The second window needs to advertise our slush, small slush 89p - Large £1.39 - Yard Cup £1.99
• Please see attached similar artwork on my previous tasks.
• It is nice to have a full bright design that will invite customers to my store whilst walking past
• I do not require a basic design, this must be top of the range professional crisp and clean.

```html
<!DOCTYPE html>
<html lang="en">
<head>
<meta charset="utf-8">
<title>Slush Window Sign</title>
<link href="https://fonts.googleapis.com/css2?family=Fredoka:wght@500;600&family=Lilita+One&display=swap" rel="stylesheet">
<style>
  :root {
    --page: #ffffff;
    --orange: #ff7a12;
    --orange-deep: #f2531c;
    --pink: #ec2f6e;
    --magenta: #e0127f;
    --price: #e3157f;
    --white: #ffffff;
    --leaf-orange: rgba(255, 150, 40, 0.55);
    --leaf-pink: rgba(205, 40, 140, 0.45);
    --title-top: #ffd23a;
    --title-bottom: #f25a12;
    --title-edge: #b3200e;
  }
  * { margin: 0; padding: 0; box-sizing: border-box; }
  html, body {
    width: 1001px; height: 1200px; overflow: hidden;
    background: var(--page);
  }
  .canvas { position: relative; width: 1001px; height: 1200px; }
  .sign {
    position: absolute; left: 126px; top: 96px; width: 748px; height: 994px;
    overflow: hidden;
    background: linear-gradient(172deg, var(--orange) 0%, var(--orange-deep) 38%, var(--pink) 72%, var(--magenta) 100%);
    box-shadow: 0 6px 22px rgba(0,0,0,0.35);
  }
  .foliage { position: absolute; border-radius: 50%; filter: blur(18px); }
  .foliage--top-right { left: 420px; top: -40px; width: 380px; height: 320px; background: var(--leaf-pink); }
  .foliage--left { left: -80px; top: 440px; width: 300px; height: 300px; background: var(--leaf-orange); }
  .foliage--right { left: 560px; top: 540px; width: 240px; height: 300px; background: var(--leaf-pink); }
  .foliage--bottom-left { left: -60px; top: 820px; width: 260px; height: 220px; background: var(--leaf-pink); }
  .glow { position: absolute; border-radius: 50%; background: radial-gradient(circle, rgba(255,255,255,0.55), rgba(255,255,255,0) 70%); }
  .label {
    position: absolute; transform: translate(-50%, -50%);
    font-family: "Fredoka", sans-serif; font-weight: 600; color: var(--white);
    text-shadow: 0 3px 6px rgba(170, 40, 0, 0.45); white-space: nowrap;
  }
  .label--small { left: 114px; top: 276px; font-size: 38px; transform: translate(-50%, -50%) rotate(-8deg); }
  .label--large { left: 326px; top: 156px; font-size: 40px; }
  .label--yard { left: 546px; top: 126px; font-size: 42px; transform: translate(-50%, -50%) rotate(4deg); }
  .price {
    position: absolute; transform: translate(-50%, -50%); border-radius: 50%;
    background: radial-gradient(circle at 40% 35%, #ffffff 55%, #fde6ee 100%);
    box-shadow: 0 0 18px rgba(255,255,255,0.55);
    display: flex; align-items: center; justify-content: center;
    font-family: "Fredoka", sans-serif; font-weight: 600; color: var(--price);
  }
  .price--small { left: 118px; top: 352px; width: 84px; height: 84px; font-size: 36px; }
  .price--large { left: 326px; top: 262px; width: 104px; height: 104px; font-size: 36px; }
  .price--yard { left: 542px; top: 242px; width: 136px; height: 136px; font-size: 44px; }
  .product-shot {
    position: absolute; left: 224px; top: 424px; width: 290px; height: 290px;
    border-radius: 40% 40% 30% 30%;
    background: linear-gradient(100deg, rgba(250,240,140,0.85) 0%, rgba(240,240,190,0.8) 45%, rgba(150,220,90,0.85) 60%, rgba(120,200,70,0.85) 100%);
    filter: blur(2px);
  }
  .title {
    position: absolute; left: 374px; top: 804px; transform: translate(-50%, -50%);
    font-family: "Lilita One", sans-serif; font-size: 150px; letter-spacing: 2px;
    color: var(--title-bottom);
    background: linear-gradient(180deg, var(--title-top) 10%, var(--title-bottom) 85%);
    -webkit-background-clip: text; background-clip: text; -webkit-text-fill-color: transparent;
    -webkit-text-stroke: 3px var(--title-edge);
    filter: drop-shadow(0 0 0 #fff) drop-shadow(6px 0 0 #fff) drop-shadow(-6px 0 0 #fff) drop-shadow(0 6px 0 #fff) drop-shadow(0 -6px 0 #fff) drop-shadow(0 8px 10px rgba(120,0,40,0.45));
  }
</style>
</head>
<body>
<div class="canvas">
  <section class="sign">
    <div class="foliage foliage--top-right" role="img" aria-label="Pink palm leaf silhouettes"></div>
    <div class="foliage foliage--left" role="img" aria-label="Orange palm leaf silhouettes"></div>
    <div class="foliage foliage--right" role="img" aria-label="Pink palm leaf silhouettes"></div>
    <div class="foliage foliage--bottom-left" role="img" aria-label="Pink palm leaf silhouettes"></div>

    <div class="glow" style="left:0;top:40px;width:200px;height:200px"></div>
    <div class="glow" style="left:-10px;top:380px;width:140px;height:140px"></div>
    <div class="glow" style="left:560px;top:340px;width:120px;height:120px"></div>
    <div class="glow" style="left:120px;top:680px;width:150px;height:150px"></div>

    <span class="label label--small">SMALL</span>
    <span class="label label--large">LARGE</span>
    <span class="label label--yard">YARD CUP</span>

    <div class="price price--small">89p</div>
    <div class="price price--large">£1.39</div>
    <div class="price price--yard">£1.99</div>

    <div class="product-shot" role="img" aria-label="Two domed slush cups with straws, one lemon yellow and one lime green"></div>

    <h1 class="title">SLUSH</h1>
  </section>
</div>
</body>
</html>
```